Modern, Clean, Edgy & Fun Comedy Show Flyer

We need to a create a new flyer for the comedy show, Harbor Laugh Night. The original version of the flyer is attached (file: Old flyer), as well as two versions of the logo.
- The text should be the same except now the show is Every First Wednesday and the next show is June 1.
- Remove the jerk shop logo
- Remove the picture of the man, and replace it with a photo of Delphine (our host), the Audience, or something of your own design.
* pictures of Delphine and the Audience is attached.
* We'd like to keep the same color palette and have also attached a color palette for reference

I have also attached 4 references of flyers that I like, that you can use to get an idea of the theme and aesthetic we are looking for.
* Files: Reference 1, Reference 2, Reference 3, Reference 4
Updates

Colors
3277b5
85acd3
0455a3
eaf1f7
cee9f5
ecf7fb
d5d5d5
e6e6e6

Requirements
Must have
• The harbor laugh night logo attached
• The text as specified in the project description
• An option with Delphine and without

```html
<!DOCTYPE html>
<html lang="en">
<head>
<meta charset="utf-8">
<title>Harbor Laugh Night – Comedy Show Every 1st Wednesday</title>
<link rel="stylesheet" href="https://fonts.googleapis.com/css2?family=Fredoka:wght@600;700&family=Signika:wght@500&family=Patrick+Hand&family=Open+Sans:wght@700;800&display=swap">
<style>
  :root {
    --ink: #0a0a0a;
    --brand-blue: #1446c8;
    --name-grey: #7a7a7a;
    --wall-light: #f6f6f6;
    --wall-mid: #e6e6e6;
    --wall-dark: #d5d5d5;
    --photo-dark: #2a1d17;
    --photo-mid: #5a4034;
  }
  * { margin: 0; padding: 0; box-sizing: border-box; }
  html, body { width: 1200px; height: 848px; overflow: hidden; background: var(--wall-mid); }

  .flyer { position: relative; width: 1200px; height: 848px; overflow: hidden; }

  .wall-backdrop {
    position: absolute; inset: 0;
    background: linear-gradient(180deg, var(--wall-light) 0%, var(--wall-mid) 55%, var(--wall-dark) 100%);
  }

  .headline {
    position: absolute; top: 12px; left: 0; width: 1200px;
    text-align: center;
    font-family: "Fredoka", sans-serif; font-weight: 700;
    font-size: 68px; letter-spacing: 1px; line-height: 90px;
    color: var(--ink);
  }
  .headline sup { font-size: 30px; vertical-align: 30px; }

  .host-photo {
    position: absolute; left: 322px; top: 98px; width: 290px; height: 750px;
    background:
      radial-gradient(ellipse 60% 22% at 50% 14%, var(--photo-mid) 0%, var(--photo-dark) 70%, transparent 100%),
      linear-gradient(180deg, transparent 0%, var(--photo-dark) 14%, var(--photo-mid) 45%, var(--photo-dark) 100%);
    -webkit-mask-image: linear-gradient(90deg, transparent 0%, #000 18%, #000 82%, transparent 100%);
            mask-image: linear-gradient(90deg, transparent 0%, #000 18%, #000 82%, transparent 100%);
  }

  .lineup { position: absolute; left: 32px; top: 250px; }
  .lineup-label {
    font-family: "Fredoka", sans-serif; font-weight: 600;
    font-size: 23px; color: var(--brand-blue); letter-spacing: 0.5px;
    margin-bottom: 38px;
  }
  .lineup-list { list-style: none; }
  .comic {
    font-family: "Signika", sans-serif; font-weight: 500;
    font-size: 42px; line-height: 69px; color: var(--brand-blue);
  }
  .comic--alt { color: var(--name-grey); text-shadow: 1px 2px 2px rgba(0,0,0,0.25); }

  .show-mark {
    position: absolute; left: 600px; top: 150px; width: 570px;
    text-align: center;
    font-family: "Fredoka", sans-serif; font-weight: 700;
    color: var(--brand-blue);
  }
  .show-mark-name { display: block; font-size: 118px; line-height: 1.05; }
  .show-mark-name span { display: block; }
  .show-mark-name .show-mark-small { font-size: 90px; }

  .event-details {
    position: absolute; left: 660px; top: 546px; width: 470px;
    text-align: center;
  }
  .event-host {
    font-family: "Patrick Hand", cursive; font-size: 40px;
    letter-spacing: 1.5px; color: var(--ink); line-height: 46px;
  }
  .event-date {
    font-family: "Open Sans", sans-serif; font-weight: 800;
    font-size: 38px; color: var(--brand-blue); line-height: 48px;
    text-shadow: 1px 2px 2px rgba(0,0,0,0.2);
    margin-bottom: 22px;
  }
  .venue-name, .venue-address, .venue-entry {
    font-family: "Open Sans", sans-serif; font-weight: 700;
    font-size: 26px; line-height: 49px;
  }
  .venue-name, .venue-entry { color: var(--ink); }
  .venue-address { color: var(--brand-blue); }
  .venue-entry .divider { display: inline-block; margin: 0 6px; }
</style>
</head>
<body>
<main class="flyer">
  <div class="wall-backdrop" role="img" aria-label="Whitewashed brick wall backdrop"></div>

  <h1 class="headline">Comedy Show Every 1<sup>st</sup> Wednesday</h1>

  <div class="host-photo" role="img" aria-label="Photo of host Delphine on stage holding a microphone"></div>

  <section class="lineup">
    <p class="lineup-label">Featuring...</p>
    <ul class="lineup-list">
      <li class="comic">Reggie Holloway</li>
      <li class="comic comic--alt">Tess Whitford</li>
      <li class="comic">Milo Brandtwood</li>
      <li class="comic comic--alt">Arjun Mehra</li>
      <li class="comic">Ruth Okafor</li>
    </ul>
  </section>

  <div class="show-mark">
    <p class="show-mark-name"><span>Harbor</span><span class="show-mark-small">Laugh Night</span></p>
  </div>

  <section class="event-details">
    <p class="event-host">Hosted by Delphine Marlow</p>
    <p class="event-date">WEDNESDAY, 1ST JUNE</p>
    <p class="venue-name">The Cardboard Loft</p>
    <p class="venue-address">42 Willow Lane, Harborview</p>
    <p class="venue-entry">Adm: FREE <span class="divider">|</span> Doors 6:30 PM</p>
  </section>
</main>
</body>
</html>
```